Building company requiring web site design

We need a web design for a new company based in Sydney called Kestrel Building Co. We build and renovate new and existing homes for consumers. We would like to see design that use the colours red and grey. The final design should communicate innovative building but with old fashion quality, great customer service and attention to detail. I have already had a logo and stationary design completed and would like to use the these colour schemes
Updates

Target Market(s)

Home owners, investors

Industry/Entity Type

Building

Coding

Coded - Design and coding required

Number of Pages Required

5+ page

Requirements
Must have
• Home page, contact page, about us page, gallery page and testimonial page
Nice to have
• Contact form

```html
<!DOCTYPE html>
<html lang="en">
<head>
<meta charset="utf-8">
<title>Kestrel Building Co</title>
<link rel="stylesheet" href="https://fonts.googleapis.com/css2?family=Raleway:wght@400;500;600&family=Open+Sans:wght@400;600&display=swap">
<style>
:root{
  --red:#b23a3f;
  --red-dark:#9c2f34;
  --grey:#8a8a8a;
  --ink:#222;
  --line:#d9d9d9;
  --white:#fff;
  --fb:#3b5b98;
  --tw:#3ea8dc;
  --gp:#d64a5b;
  --mail:#4a5670;
}
*{margin:0;padding:0;box-sizing:border-box}
html,body{width:1200px;height:2535px;overflow:hidden;background:var(--white)}
body{position:relative;font-family:"Open Sans",Arial,sans-serif;color:var(--ink)}
.abs{position:absolute}

.brand{left:0;width:1200px;top:40px;display:flex;justify-content:center;align-items:center;gap:14px}
.brand-mark{width:34px;height:34px;background:var(--red)}
.brand-name{font-family:"Raleway",sans-serif;font-weight:600;font-size:34px;color:var(--ink)}

.main-nav{left:302px;width:596px;top:155px;height:38px;border-top:2px solid var(--line);border-bottom:2px solid var(--line);display:flex;justify-content:space-around;align-items:center;font-size:16px}
.main-nav a{color:var(--ink);text-decoration:none}

.hero{left:85px;top:220px;width:1030px;height:438px;background:linear-gradient(135deg,#7a5a48 0%,#b9a28a 40%,#e7d9b8 55%,#4f7fb8 80%,#8c6f55 100%)}
.hero-arrow{top:417px;width:42px;height:42px;border-radius:50%;background:var(--white);display:flex;align-items:center;justify-content:center}
.hero-arrow.prev{left:133px}.hero-arrow.next{left:1033px}

.section-title{left:0;width:1200px;text-align:center;font-family:"Raleway",sans-serif;font-weight:500;color:var(--red)}
.about-title{top:690px;font-size:36px}
.title-rule{left:560px;width:80px;height:2px;background:var(--red);top:738px}
.lead{left:210px;width:780px;text-align:center;font-size:14px;line-height:26px}

.services-band{left:85px;top:875px;width:1030px;height:238px;display:flex}
.services-photo{width:516px;height:100%;background:linear-gradient(160deg,#cfe0ec 0%,#8fa7b8 45%,#5b6b73 100%)}
.services-list{flex:1;background:var(--red);color:var(--white);list-style:none;padding:14px 18px 14px 22px;font-size:11.5px;line-height:23px;display:flex;flex-direction:column;justify-content:center}
.services-list li{padding-left:16px;text-indent:-16px}
.services-list li::before{content:"";display:inline-block;width:5px;height:5px;background:var(--white);border-radius:50%;margin-right:11px;vertical-align:middle;text-indent:0}

.service{width:260px;text-align:center}
.service svg{display:block;margin:0 auto}
.service-label{font-family:"Raleway",sans-serif;font-size:28px;color:var(--red);margin-top:22px}

.divider{left:85px;width:1030px;top:1646px;height:1px;background:var(--line)}
.gallery-title{top:1692px;font-size:42px}
.gallery-item{width:248px;height:178px;border-radius:4px}

.footer{left:85px;top:2276px;width:1030px;height:237px;background:var(--red);color:var(--white)}
.footer h3{font-family:"Raleway",sans-serif;font-weight:400;font-size:22px;position:absolute;top:38px}
.footer p,.footer li{font-size:12px;line-height:19px}
.footer ul{list-style:none}
.footer-col{position:absolute;top:80px}
.footer-sep{position:absolute;top:45px;width:1px;height:140px;background:rgba(255,255,255,.5)}
.social{position:absolute;top:80px;left:42px;display:flex}
.social div{width:66px;height:96px;display:flex;align-items:flex-end;justify-content:center;padding-bottom:8px;font-size:13px}
.copyright{position:absolute;bottom:14px;left:0;width:100%;text-align:center;font-size:11px}
</style>
</head>
<body>

<header>
  <div class="abs brand"><span class="brand-mark"></span><span class="brand-name">Kestrel Building Co</span></div>
  <nav class="abs main-nav">
    <a href="#">Home</a><a href="#">About us</a><a href="#">Gallery</a><a href="#">Testimonial</a><a href="#">Contact us</a>
  </nav>
</header>

<div class="abs hero" role="img" aria-label="Builder in hard hat reviewing house plans with a smiling couple outside a home"></div>
<div class="abs hero-arrow prev"><svg width="16" height="16" viewBox="0 0 16 16"><path d="M10 3 5 8l5 5" fill="none" stroke="#222" stroke-width="2"/></svg></div>
<div class="abs hero-arrow next"><svg width="16" height="16" viewBox="0 0 16 16"><path d="M6 3l5 5-5 5" fill="none" stroke="#222" stroke-width="2"/></svg></div>

<h2 class="abs section-title about-title">About us</h2>
<div class="abs title-rule"></div>
<p class="abs lead" style="top:752px">Lorem Ipsum is simply dummy text of the printing and typesetting industry. Lorem Ipsum has been the industry's standard dummy text ever since the 1500s, when an unknown printer took a galley of type and scrambled it to make a type specimen book.</p>

<section class="abs services-band">
  <div class="services-photo" role="img" aria-label="Two engineers in hard hats inside a modern glass building"></div>
  <ul class="services-list">
    <li>Building new homes and renovating existing homes</li>
    <li>Installing new kitchens and bathrooms, and renovating kitchens and bathrooms</li>
    <li>Design service</li>
    <li>Office fit outs</li>
    <li>All aspects of insurance repair work from rebuilding burnt out houses to reinstating fences</li>
    <li>Light commercial work</li>
    <li>Roofing</li>
  </ul>
</section>

<div class="abs service" style="left:155px;top:1163px">
  <svg width="130" height="130" viewBox="0 0 130 130"><rect x="20" y="20" width="90" height="90" transform="rotate(45 65 65)" fill="#b23a3f"/><path d="M52 52l26 26M78 52 52 78" stroke="#fff" stroke-width="4" stroke-linecap="round"/><circle cx="50" cy="50" r="5" fill="none" stroke="#fff" stroke-width="3"/><circle cx="80" cy="80" r="5" fill="none" stroke="#fff" stroke-width="3"/></svg>
  <div class="service-label">Maintenance</div>
</div>
<div class="abs service" style="left:471px;top:1163px">
  <svg width="130" height="130" viewBox="0 0 130 130"><rect x="22" y="22" width="86" height="86" transform="rotate(45 65 65)" fill="none" stroke="#222" stroke-width="2"/><circle cx="65" cy="65" r="12" fill="none" stroke="#222" stroke-width="3"/><path d="M61 60v6M69 60v6M65 70v6" stroke="#222" stroke-width="3"/></svg>
  <div class="service-label">Wiring</div>
</div>
<div class="abs service" style="left:765px;top:1163px">
  <svg width="130" height="130" viewBox="0 0 130 130"><rect x="22" y="22" width="86" height="86" transform="rotate(45 65 65)" fill="none" stroke="#222" stroke-width="2"/><rect x="53" y="52" width="24" height="26" fill="none" stroke="#222" stroke-width="3"/><path d="M53 65h24M62 58h6M62 71h6" stroke="#222" stroke-width="2"/></svg>
  <div class="service-label">Tiling</div>
</div>
<div class="abs service" style="left:155px;top:1394px">
  <svg width="130" height="130" viewBox="0 0 130 130"><rect x="22" y="22" width="86" height="86" transform="rotate(45 65 65)" fill="none" stroke="#222" stroke-width="2"/><circle cx="65" cy="65" r="13" fill="none" stroke="#222" stroke-width="3"/><path d="M65 52v26M52 65h26M56 56l18 18M74 56 56 74" stroke="#222" stroke-width="2"/></svg>
  <div class="service-label">Audio/Visual</div>
</div>
<div class="abs service" style="left:471px;top:1394px">
  <svg width="130" height="130" viewBox="0 0 130 130"><rect x="22" y="22" width="86" height="86" transform="rotate(45 65 65)" fill="none" stroke="#222" stroke-width="2"/><path d="M58 52v10M68 52v10M54 62h18v6a9 9 0 0 1-18 0zM63 77v8" fill="none" stroke="#222" stroke-width="3"/></svg>
  <div class="service-label">Electrical</div>
</div>
<div class="abs service" style="left:765px;top:1394px">
  <svg width="130" height="130" viewBox="0 0 130 130"><rect x="22" y="22" width="86" height="86" transform="rotate(45 65 65)" fill="none" stroke="#222" stroke-width="2"/><path d="M50 58h20a6 6 0 0 1 6 6v6M60 52v6M54 52h12" fill="none" stroke="#222" stroke-width="3"/><path d="M76 76v4" stroke="#222" stroke-width="3"/></svg>
  <div class="service-label">Plumbing</div>
</div>

<div class="abs divider"></div>

<h2 class="abs section-title gallery-title">Our Gallery</h2>
<p class="abs lead" style="top:1756px">Lorem Ipsum is simply dummy text of the printing and typesetting industry. Lorem Ipsum has been the industry's.</p>

<div class="abs gallery-item" style="left:186px;top:1816px;background:linear-gradient(135deg,#6b4a2e,#c99b5e)" role="img" aria-label="Ornate wrought iron spiral staircase"></div>
<div class="abs gallery-item" style="left:466px;top:1816px;background:linear-gradient(135deg,#e9edf0,#5a6670)" role="img" aria-label="Modern kitchen sink with chrome tap"></div>
<div class="abs gallery-item" style="left:748px;top:1816px;background:linear-gradient(135deg,#d9c6ae,#6f9cc8)" role="img" aria-label="Room being painted with a ladder and pendant lights"></div>
<div class="abs gallery-item" style="left:186px;top:2028px;background:linear-gradient(135deg,#5d86b8,#e8e2d8)" role="img" aria-label="White two storey house exterior"></div>
<div class="abs gallery-item" style="left:466px;top:2028px;background:linear-gradient(135deg,#f1e6d6,#a05a2c)" role="img" aria-label="Timber spiral staircase viewed from above"></div>
<div class="abs gallery-item" style="left:748px;top:2028px;background:linear-gradient(135deg,#c7a98a,#4e5d6e)" role="img" aria-label="Renovated bedroom interior"></div>

<footer class="abs footer">
  <h3 style="left:42px">Follow Us</h3>
  <div class="social">
    <div style="background:var(--fb)">248k</div>
    <div style="background:var(--tw)">36k</div>
    <div style="background:var(--gp)">124k</div>
    <div style="background:var(--mail)">85k</div>
  </div>
  <div class="footer-sep" style="left:335px"></div>
  <h3 style="left:393px">About us</h3>
  <p class="footer-col" style="left:393px;width:210px">Lorem Ipsum is simply dummy text of the printing and typesetting industry. Lorem Ipsum has been the industry's standard dummy text ever since the 1500s.</p>
  <div class="footer-sep" style="left:627px"></div>
  <h3 style="left:641px">Links</h3>
  <ul class="footer-col" style="left:641px"><li>Knowledge Base</li><li>Jobs</li><li>Press</li><li>Terms of services</li></ul>
  <div class="footer-sep" style="left:782px"></div>
  <h3 style="left:810px">Newsletter Archive</h3>
  <p class="footer-col" style="left:810px;width:190px">Click here to access our latest newsletters</p>
  <p class="footer-col" style="left:820px;top:138px">Building Newsletter Archive</p>
  <p class="copyright">Copyright © 2012 Kestrel Building Co.</p>
</footer>

</body>
</html>
```